Photography business needs a money-off coupon design to be sent out by text

I'm a headshot photographer and I want to start a 'refer a friend' programme. Each time I take someone's headshot, I want to be able to give them a money-off coupon, featuring their own headshot, that they can send to their own network by text, offering a 20% discount to the recipient on a headshot session.

I need the design as a layered PSD file, so that I can drop in a different headshot for each client. Because the coupon will be being sent by text, I need it to be as simple and striking as possible. The design should meet the following criteria:

- It should feature my logo (two versions attached)

- It should feature one headshot - needs to be the main feature of the design. I have attached three examples from a typical session - as you will see, I use different backgrounds, so the design should be able to accommodate different colours.

- The following copy:

Milo Gives You 20% off (name will change with different headshots)

£30 off your next headshot session
Just text this referral card to make your appointment
Owen Clarke 07942 618 407
Normal Price £150, Now £130
www.lenvaprint.co.uk

- The design should be portrait rather than landscape, given that that's how most people tend to use their phones vertically when they first look at a text message

- I need the designer to think about how the coupon will render on mobile phones; I think that it probably makes most sense to size the image in line with whichever smartphone has the highest resolution screen (probably orbix t4 or pad 7), as that way the image will look good on all phone screens. Although I am happy to take the designer's advice on this and on optimum aspect ratio.

- Any other advice the designer can give me about the optimal design for text marketing of this nature will strongly impact on my final decision.

PLEASE NOTE: I've just uploaded a very basic layout that I did in Adobe Spark - I'm not expecting designers to follow it, but it does contain the key elements

Thanks,

Owen

Target Market(s)

Actors

Industry/Entity Type

Photographer

Font styles to use
Sans Serif

Colors

Designer to choose colors to be used in the design.

Requirements
Must have
• Clear communication of discount and redemption mechanism. Headshot image to be the most prominent feature. Must render clearly in different types of smartphone
Nice to have
• If possible, a link to my website (don't know if this is technically possible)
Should not have
• Colours which clash with my logo / the featured image

```html
<!DOCTYPE html>
<html lang="en">
<head>
<meta charset="utf-8">
<title>Refer a Friend Coupon</title>
<link rel="stylesheet" href="https://fonts.googleapis.com/css2?family=Oswald:wght@400;500&family=EB+Garamond:ital,wght@0,400;1,400;1,700&family=Luckiest+Guy&family=Arimo:wght@400&display=swap">
<style>
  :root {
    --page: #f1f1f1;
    --gold: #dcaa5c;
    --gold-deep: #c98f3a;
    --band-light: #ebc685;
    --band-mid: #deb066;
    --brown: #6b4719;
    --brown-dark: #5a3a12;
    --cream: #f6e6c4;
    --navy: #1d2c4a;
    --skin: #e3b396;
    --hair: #3e3029;
  }
  html, body {
    margin: 0;
    width: 1200px;
    height: 800px;
    overflow: hidden;
    background: var(--page);
  }
  .coupon {
    position: absolute;
    left: 384px;
    top: 16px;
    width: 432px;
    height: 768px;
    overflow: hidden;
    font-family: "Oswald", sans-serif;
    color: var(--brown);
  }
  .headshot {
    position: absolute;
    left: 0; right: 0; top: 0;
    height: 540px;
    background:
      radial-gradient(ellipse 26% 17% at 50% 15%, var(--hair) 0%, rgba(62,48,41,0.85) 55%, rgba(62,48,41,0) 100%),
      radial-gradient(ellipse 25% 30% at 49% 44%, var(--skin) 0%, rgba(227,179,150,0.9) 55%, rgba(227,179,150,0) 100%),
      radial-gradient(ellipse 20% 14% at 48% 78%, rgba(214,160,128,0.95) 0%, rgba(214,160,128,0) 100%),
      linear-gradient(180deg, rgba(29,44,74,0) 0%, rgba(29,44,74,0) 76%, var(--navy) 90%, var(--navy) 100%),
      radial-gradient(ellipse at 45% 35%, #e7b96a 0%, var(--gold) 50%, var(--gold-deep) 100%);
  }
  .brand {
    position: absolute;
    right: 12px;
    top: 14px;
    display: flex;
    align-items: center;
    gap: 6px;
    font-family: "Oswald", sans-serif;
    font-weight: 500;
    font-size: 18px;
    letter-spacing: 0.5px;
    text-transform: uppercase;
    color: var(--brown);
  }
  .brand-square {
    width: 14px;
    height: 14px;
    border: 3px solid var(--brown);
    box-sizing: border-box;
  }
  .share-joy {
    position: absolute;
    left: 296px;
    top: 460px;
    width: 110px;
    text-align: center;
    color: var(--gold);
    line-height: 0.95;
  }
  .share-joy .share { font-family: "Luckiest Guy", Impact, sans-serif; font-size: 33px; }
  .share-joy .joy { font-family: "Luckiest Guy", Impact, sans-serif; font-size: 21px; }
  .share-joy .refer {
    font-family: "Arimo", sans-serif;
    font-size: 10px;
    margin-top: 4px;
    letter-spacing: 0.3px;
  }
  .offer-band {
    position: absolute;
    left: 0; right: 0; bottom: 0;
    height: 228px;
    background: linear-gradient(180deg, var(--band-mid) 0%, var(--band-light) 100%);
  }
  .offer-title {
    position: absolute;
    left: 24px;
    top: 10px;
    font-size: 29px;
    font-weight: 400;
    line-height: 1.1;
    transform: scaleX(0.86);
    transform-origin: left;
    white-space: nowrap;
  }
  .price-line {
    position: absolute;
    left: 42px;
    top: 46px;
    font-size: 20px;
    white-space: nowrap;
    transform: scaleX(0.88);
    transform-origin: left;
  }
  .price-now {
    display: inline-block;
    margin-left: 8px;
    font-size: 23px;
    padding: 0 3px;
    border-top: 2px solid var(--brown);
    border-left: 2px solid var(--brown);
    line-height: 1.05;
    position: relative;
  }
  .price-now::after {
    content: "";
    position: absolute;
    right: -4px;
    bottom: -2px;
    width: 8px;
    height: 10px;
    border-right: 2px solid var(--brown);
    border-bottom: 2px solid var(--brown);
  }
  .redeem-note {
    position: absolute;
    left: 30px;
    top: 82px;
    width: 210px;
    text-align: center;
    font-family: "EB Garamond", serif;
    font-style: italic;
    font-size: 15px;
    line-height: 1.15;
  }
  .contact-name {
    position: absolute;
    left: 60px;
    top: 126px;
    width: 160px;
    text-align: center;
    font-family: "EB Garamond", serif;
    font-style: italic;
    font-weight: 700;
    font-size: 19px;
  }
  .phone-icon {
    position: absolute;
    left: 36px;
    top: 154px;
  }
  .phone-pill {
    position: absolute;
    left: 60px;
    top: 157px;
    width: 162px;
    height: 27px;
    border-radius: 14px;
    background: var(--brown);
    color: var(--cream);
    font-family: "EB Garamond", serif;
    font-size: 20px;
    line-height: 27px;
    text-align: center;
    letter-spacing: 0.5px;
  }
  .website {
    position: absolute;
    left: 36px;
    top: 194px;
    font-family: "EB Garamond", serif;
    font-size: 17px;
    color: var(--brown-dark);
  }
  .photographer-art {
    position: absolute;
    right: 12px;
    bottom: 0;
    width: 150px;
    height: 176px;
    border-radius: 50% 50% 0 0 / 30% 30% 0 0;
    background: linear-gradient(180deg, rgba(122,85,48,0.85) 0%, #a7c04a 50%, #8db236 100%);
  }
</style>
</head>
<body>
  <main class="coupon">
    <div class="headshot" role="img" aria-label="Client headshot: young man with dark swept hair in a navy t-shirt, on a warm gold studio backdrop"></div>

    <div class="brand"><span class="brand-square"></span>Lenva Print</div>

    <div class="share-joy">
      <div class="share">SHARE</div>
      <div class="joy">THE JOY</div>
      <div class="refer">REFER A FRIEND</div>
    </div>

    <section class="offer-band">
      <div class="offer-title">£30 OFF YOUR NEXT HEADSHOT SESSION</div>
      <div class="price-line">NORMAL PRICE £150 <span class="price-now">NOW £130</span></div>
      <div class="redeem-note">Just text this referral card to<br>make your appointment</div>
      <div class="contact-name">Owen Clarke</div>
      <svg class="phone-icon" width="22" height="34" viewBox="0 0 22 34" aria-hidden="true">
        <rect x="1" y="1" width="20" height="32" rx="4" fill="var(--brown)"/>
        <rect x="4" y="5" width="14" height="22" rx="1" fill="var(--band-light)"/>
        <circle cx="11" cy="30" r="1.5" fill="var(--band-light)"/>
      </svg>
      <div class="phone-pill">07942 618 407</div>
      <div class="website">www.lenvaprint.co.uk</div>
      <div class="photographer-art" role="img" aria-label="Illustration of a photographer in a hat holding a camera"></div>
    </section>
  </main>
</body>
</html>
```